New Web Design Project

See attachments on the content and concept. Very important that the flow of the tiers stand out

Target Market(s)

Food and Beverage Manufacturing

Industry/Entity Type

Food and Beverage

Coding

Coded - Design and coding required

Number of Pages Required

3 page

Colors
0054AA
0677BA
7BADD7
CADEEF
E8F1F8

```html
<!DOCTYPE html>
<html lang="en">
<head>
<meta charset="utf-8">
<title>Northbay Compliance Group – SQF Consulting</title>
<link href="https://fonts.googleapis.com/css2?family=Libre+Baskerville:wght@400;700&family=Poppins:wght@400;500;600;700&display=swap" rel="stylesheet">
<style>
:root{
  --navy:#17165a;
  --navy-deep:#13124a;
  --royal:#1d1ce0;
  --royal-soft:#4442e8;
  --lav:#b6b4f2;
  --lav-soft:#ecebfc;
  --lav-pale:#f5f5fd;
  --ink:#1c1c3a;
  --body:#55566b;
  --white:#ffffff;
  --photo-a:#c9ccd6;
  --photo-b:#8e96a8;
}
*{box-sizing:border-box;margin:0;padding:0}
html,body{width:1200px;height:3755px;overflow:hidden}
body{position:relative;background:var(--white);font-family:'Poppins',sans-serif;color:var(--ink)}
.serif{font-family:'Libre Baskerville',serif}
.abs{position:absolute}

/* nav */
.site-nav{position:absolute;left:0;top:0;width:1200px;height:58px;background:var(--white)}
.brand{position:absolute;display:flex;align-items:center;gap:9px}
.brand-dot{width:32px;height:32px;border-radius:50%;border:2px solid var(--royal)}
.brand-name{font-family:'Libre Baskerville',serif;font-weight:700;font-size:13px;color:var(--navy);line-height:1.1}
.brand-tag{font-size:8px;letter-spacing:.8px;color:var(--navy);margin-top:2px}
.nav-links a{position:absolute;top:22px;font-size:11px;font-weight:500;color:var(--ink);text-decoration:none;letter-spacing:.3px}
.nav-links a.active{color:var(--royal)}
.btn{position:absolute;display:flex;align-items:center;justify-content:center;gap:8px;font-size:11px;font-weight:500;letter-spacing:.3px;border-radius:4px;text-decoration:none}
.btn svg{width:14px;height:14px}
.btn-royal{background:var(--royal);color:var(--white)}

/* hero */
.hero{position:absolute;left:0;top:58px;width:1200px;height:760px}
.hero-bg{position:absolute;left:0;top:0}
.hero h1{position:absolute;left:121px;top:102px;width:560px;font-family:'Libre Baskerville',serif;font-weight:400;font-size:44px;line-height:47px;color:var(--white)}
.hero h1 em{font-style:normal;color:var(--lav)}
.hero-lead{position:absolute;left:121px;top:303px;width:490px;font-size:11px;line-height:17px;color:#e3e3f7}
.btn-lav{background:var(--lav);color:var(--navy)}
.btn-ghost{border:1px solid #cfcff0;color:var(--white)}

/* stats */
.stat{position:absolute;width:198px;height:198px;border-radius:50%;background:radial-gradient(circle at 50% 40%,#ffffff 55%,#efeffc 100%);box-shadow:0 6px 18px rgba(60,60,160,.12);text-align:center}
.stat-tick{position:absolute;left:86px;top:-7px;width:26px;height:26px}
.stat-num{position:absolute;left:0;width:100%;top:79px;font-weight:700;font-size:31px;color:var(--navy)}
.stat-label{position:absolute;left:0;width:100%;top:124px;font-size:12.5px;color:var(--ink)}

.watermark{position:absolute;left:0;width:1200px;top:960px;text-align:center;font-family:'Libre Baskerville',serif;font-size:86px;color:transparent;-webkit-text-stroke:1px #ecebf8;white-space:nowrap}

/* services */
.services{position:absolute;left:0;top:1042px;width:1200px;height:693px;background:linear-gradient(180deg,var(--lav-pale) 0%,#f1f0fd 70%,#e3e2fb 100%)}
.section-title{position:absolute;left:0;width:1200px;text-align:center;font-family:'Libre Baskerville',serif;font-size:31px;color:var(--ink)}
.section-sub{position:absolute;left:0;width:1200px;text-align:center;font-size:11.5px;line-height:17px;color:var(--body)}
.eyebrow{position:absolute;left:0;width:1200px;text-align:center;font-size:10.5px;font-weight:500;color:var(--royal);letter-spacing:.3px}
.card{position:absolute;width:303px;height:227px;background:var(--white);border:1px solid #e6e5f7;border-radius:8px 8px 8px 46px;box-shadow:0 4px 14px rgba(60,60,160,.06);text-align:center}
.card-icon{position:absolute;left:124px;top:24px;width:54px;height:58px}
.card h3{position:absolute;left:0;width:100%;top:92px;font-size:15px;font-weight:500;color:var(--ink)}
.card p{position:absolute;left:40px;right:40px;top:116px;font-size:10.5px;line-height:17.5px;color:var(--body)}

/* why */
.why{position:absolute;left:0;top:1735px;width:1200px;height:744px;background:linear-gradient(180deg,#fff 0%,#fff 70%,#f3f2fd 100%)}
.feature{position:absolute;width:260px}
.feature h4{font-size:14.5px;font-weight:500;color:var(--ink);margin-bottom:4px}
.feature p{font-size:10.5px;line-height:17.5px;color:var(--body)}
.feature.left{text-align:right}

/* process */
.process{position:absolute;left:0;top:2479px;width:1200px;height:440px;background:var(--white)}
.step-num{position:absolute;top:156px;font-size:66px;font-weight:600;color:transparent;-webkit-text-stroke:1.2px #d9d8f6;line-height:1}
.step{position:absolute;top:236px}
.step h4{font-size:14.5px;font-weight:500;color:var(--ink);display:flex;align-items:center;gap:7px;margin-bottom:4px}
.step h4::before{content:"";width:7px;height:7px;border-radius:50%;background:var(--royal)}
.step p{font-size:10.5px;line-height:17.5px;color:var(--body)}

/* testimonial */
.testimonial{position:absolute;left:124px;top:2909px;width:952px;height:335px;border:1px solid #e6e5f7;border-radius:4px 4px 60px 4px;background:var(--white)}
.testimonial-panel{position:absolute;left:6px;top:6px;width:940px;height:322px;background:var(--lav);border-radius:2px 2px 56px 2px}
.quote-mark{position:absolute;left:42px;top:6px;font-family:'Libre Baskerville',serif;font-size:150px;line-height:1;color:#9d9ae8}
.quote-text{position:absolute;left:42px;top:124px;width:400px;font-family:'Libre Baskerville',serif;font-size:19px;line-height:29px;color:var(--white)}
.quote-cite{position:absolute;left:42px;top:282px;font-size:10.5px;color:var(--white)}
.photo{background:linear-gradient(135deg,var(--photo-a),var(--photo-b))}
.testimonial-photo{position:absolute;left:511px;top:18px;width:416px;height:292px;border:4px solid var(--white);border-radius:2px 2px 52px 2px}

/* cta + footer */
.footer-bg{position:absolute;left:0;top:3360px}
.cta{position:absolute;left:124px;top:3305px;width:952px;height:187px;background:var(--royal);border-radius:4px;text-align:center}
.cta h2{position:absolute;left:0;width:100%;top:40px;font-family:'Libre Baskerville',serif;font-weight:400;font-size:31px;color:var(--white)}
.cta p{position:absolute;left:0;width:100%;top:92px;font-size:11px;color:#dcdcfb}
.btn-white{background:var(--white);color:var(--navy)}
.footer-col-rule{position:absolute;top:3540px;width:1px;height:185px;background:#34337a}
.footer h5{position:absolute;font-family:'Libre Baskerville',serif;font-weight:400;font-size:15px;color:var(--white)}
.footer-about{position:absolute;left:130px;top:3596px;width:210px;font-size:9px;line-height:15px;color:#d5d5ee}
.foot-link{position:absolute;left:446px;font-size:9.5px;color:#d5d5ee}
.foot-row{position:absolute;display:flex;align-items:center;gap:10px;font-size:9.5px;color:#d5d5ee}
.foot-ic{width:20px;height:20px;border-radius:50%;border:1px solid #d5d5ee;display:flex;align-items:center;justify-content:center}
.foot-ic svg{width:10px;height:10px}
.copyright{position:absolute;left:0;width:1200px;top:3733px;text-align:center;font-size:9px;color:#d5d5ee}
</style>
</head>
<body>

<header class="site-nav">
  <div class="brand" style="left:121px;top:10px">
    <span class="brand-dot"></span>
    <div><div class="brand-name">Northbay Compliance Group</div><div class="brand-tag">FOOD SAFETY &amp; SQF CERTIFICATION</div></div>
  </div>
  <nav class="nav-links">
    <a class="active" style="left:380px">HOME</a>
    <a style="left:471px">SERVICES</a>
    <a style="left:580px">BENEFITS</a>
    <a style="left:687px">PROCESS</a>
    <a style="left:795px">CONTACT</a>
  </nav>
  <a class="btn btn-royal" style="left:891px;top:10px;width:185px;height:36px">GET SQF CONSULTATION
    <svg viewBox="0 0 16 16" fill="none" stroke="currentColor" stroke-width="1.3"><path d="M8 1.5l5.5 2v4.2c0 3.3-2.4 5.6-5.5 6.8-3.1-1.2-5.5-3.5-5.5-6.8V3.5z"/><path d="M5.6 8l1.7 1.7 3.2-3.3"/></svg></a>
</header>

<section class="hero">
  <svg class="hero-bg" width="1200" height="760" viewBox="0 0 1200 760">
    <defs><linearGradient id="heroGrad" x1="0" y1="0" x2="1" y2="1"><stop offset="0" stop-color="#2b2a86"/><stop offset=".6" stop-color="#1b1a64"/><stop offset="1" stop-color="#141355"/></linearGradient>
    <linearGradient id="heroPhoto" x1="0" y1="0" x2="1" y2="1"><stop offset="0" stop-color="#d6dae3"/><stop offset="1" stop-color="#8f98ab"/></linearGradient></defs>
    <path d="M0 0H1200V452Q600 744 0 452Z" fill="url(#heroGrad)"/>
    <path d="M0 468Q600 790 1200 468" fill="none" stroke="var(--royal)" stroke-width="4"/>
    <path d="M862 52L1070 160V360Q1070 470 862 508Q654 470 654 360V160Z" fill="#3a39a0"/>
    <path d="M862 72L1050 170V356Q1050 452 862 488Q674 452 674 356V170Z" fill="#ffffff"/>
    <path d="M862 104L1020 186V350Q1020 430 862 462Q704 430 704 350V186Z" fill="#1b1a64"/>
    <path d="M862 114L1010 192V348Q1010 422 862 452Q714 422 714 348V192Z" fill="url(#heroPhoto)" role="img" aria-label="Photo of food plant staff in lab coats and hairnets working at a production line"/>
  </svg>
  <h1>Hire a tech driven SQF team that carries you across the <em>Certification</em> finish line.</h1>
  <p class="hero-lead">At Northbay Compliance Group, we focus exclusively on SQF-combining real plant experience with smart technology so your team can stay focused on production while we handle the path to certification and beyond.</p>
  <a class="btn btn-lav" style="left:121px;top:381px;width:187px;height:41px">GET SQF CONSULTATION
    <svg viewBox="0 0 16 16" fill="none" stroke="currentColor" stroke-width="1.3"><path d="M8 1.5l5.5 2v4.2c0 3.3-2.4 5.6-5.5 6.8-3.1-1.2-5.5-3.5-5.5-6.8V3.5z"/><path d="M5.6 8l1.7 1.7 3.2-3.3"/></svg></a>
  <a class="btn btn-ghost" style="left:316px;top:381px;width:155px;height:41px">EXPLORE SERVICES
    <svg viewBox="0 0 16 16" fill="none" stroke="currentColor" stroke-width="1.3"><path d="M8 1.5l5.5 2v4.2c0 3.3-2.4 5.6-5.5 6.8-3.1-1.2-5.5-3.5-5.5-6.8V3.5z"/><path d="M5.6 8l1.7 1.7 3.2-3.3"/></svg></a>
</section>

<div class="stat" style="left:203px;top:726px"><svg class="stat-tick" viewBox="0 0 26 26"><circle cx="13" cy="13" r="12" fill="var(--royal)"/><circle cx="13" cy="13" r="7.5" fill="none" stroke="#fff" stroke-width="1.5"/><path d="M9.8 13l2.2 2.2 4-4" fill="none" stroke="#fff" stroke-width="1.6"/></svg><div class="stat-num">15+</div><div class="stat-label">Client Onboarding?</div></div>
<div class="stat" style="left:401px;top:726px"><svg class="stat-tick" viewBox="0 0 26 26"><circle cx="13" cy="13" r="12" fill="var(--royal)"/><circle cx="13" cy="13" r="7.5" fill="none" stroke="#fff" stroke-width="1.5"/><path d="M9.8 13l2.2 2.2 4-4" fill="none" stroke="#fff" stroke-width="1.6"/></svg><div class="stat-num">100%</div><div class="stat-label">SQF focused</div></div>
<div class="stat" style="left:599px;top:726px"><svg class="stat-tick" viewBox="0 0 26 26"><circle cx="13" cy="13" r="12" fill="var(--royal)"/><circle cx="13" cy="13" r="7.5" fill="none" stroke="#fff" stroke-width="1.5"/><path d="M9.8 13l2.2 2.2 4-4" fill="none" stroke="#fff" stroke-width="1.6"/></svg><div class="stat-num">Digital</div><div class="stat-label">Platform built Programs</div></div>
<div class="stat" style="left:798px;top:726px"><svg class="stat-tick" viewBox="0 0 26 26"><circle cx="13" cy="13" r="12" fill="var(--royal)"/><circle cx="13" cy="13" r="7.5" fill="none" stroke="#fff" stroke-width="1.5"/><path d="M9.8 13l2.2 2.2 4-4" fill="none" stroke="#fff" stroke-width="1.6"/></svg><div class="stat-num">US</div><div class="stat-label">Nationwide Coverage</div></div>

<section class="services">
  <h2 class="section-title" style="top:50px">SQF Consulting, Implementation &amp; Onboarding</h2>
  <p class="section-sub" style="top:92px">We help food and beverage manufacturers achieve and maintain SQF certification with confidence,<br>using practical programs and digital tools that work on the floor not just on audit day..</p>

  <article class="card" style="left:124px;top:154px"><svg class="card-icon" viewBox="0 0 54 58" fill="none" stroke="var(--royal)" stroke-width="1.6"><path d="M27 3l22 9v18c0 13-10 22-22 26C15 52 5 43 5 30V12z"/><circle cx="27" cy="29" r="11"/><circle cx="27" cy="29" r="4"/></svg><h3>SOF Program Design</h3><p>We design your complete SQF system from scratch - HACCP/food safety plans, prerequisite programs, SOPs, forms, logs, and all required documentation tailored to your facility.</p></article>
  <article class="card" style="left:449px;top:154px"><svg class="card-icon" viewBox="0 0 54 58" fill="none" stroke="var(--royal)" stroke-width="1.6"><path d="M27 3l22 9v18c0 13-10 22-22 26C15 52 5 43 5 30V12z"/><circle cx="27" cy="29" r="11"/><path d="M16 29h22M27 18v22"/></svg><h3>Digital Platform Build</h3><p>We build your SQF program directly into modern food safety software like PlantLedger or SafeSheet.io –digitizing forms, checklists, monitoring logs, and workflows so your team runs paperless.</p></article>
  <article class="card" style="left:773px;top:154px"><svg class="card-icon" viewBox="0 0 54 58" fill="none" stroke="var(--royal)" stroke-width="1.6"><path d="M27 3l22 9v18c0 13-10 22-22 26C15 52 5 43 5 30V12z"/><circle cx="27" cy="24" r="5"/><path d="M17 37c2-5 6-7 10-7s8 2 10 7"/></svg><h3>Coaching &amp; Support</h3><p>After building your system, we coach your team to own and maintain it day to-day. You run the program; we provide ongoing expert guidance so you stay audit-ready at all times.</p></article>
  <article class="card" style="left:124px;top:401px"><svg class="card-icon" viewBox="0 0 54 58" fill="none" stroke="var(--royal)" stroke-width="1.6"><path d="M27 3l22 9v18c0 13-10 22-22 26C15 52 5 43 5 30V12z"/><rect x="19" y="18" width="16" height="21" rx="1"/><path d="M22 24h10M22 29h10M22 34h6"/></svg><h3>Gap Assessments</h3><p>We evaluate where your facility stands against SQF requirements, identify gaps, and provide a clear roadmap to close them before your audit no surprises on certification day.</p></article>
  <article class="card" style="left:449px;top:401px"><svg class="card-icon" viewBox="0 0 54 58" fill="none" stroke="var(--royal)" stroke-width="1.6"><path d="M27 3l22 9v18c0 13-10 22-22 26C15 52 5 43 5 30V12z"/><circle cx="27" cy="24" r="4"/><circle cx="18" cy="28" r="3"/><circle cx="36" cy="28" r="3"/><path d="M19 38c1-4 4-6 8-6s7 2 8 6"/></svg><h3>Bilingual Team Support</h3><p>Our team in Central America supports Spanish-speaking employees within your operation delivering training, documentation, and coaching in the language your floor team actually speaks.</p></article>
  <article class="card" style="left:773px;top:401px"><svg class="card-icon" viewBox="0 0 54 58" fill="none" stroke="var(--royal)" stroke-width="1.6"><path d="M27 3l22 9v18c0 13-10 22-22 26C15 52 5 43 5 30V12z"/><rect x="19" y="17" width="16" height="22" rx="1"/><path d="M23 23h8M23 28h8"/><circle cx="33" cy="36" r="3"/></svg><h3>Sanitation &amp; Regulatory</h3><p>Sanitation &amp; RegulatoryFrom sanitation program design to environmental monitoring, we help you build internal capabilities that meet USDA, FDA, and FSMA requirements and reduce dependence on external contractors.</p></article>
</section>

<section class="why">
  <div class="eyebrow" style="top:58px">WHY NORTHBAY COMPLIANCE</div>
  <h2 class="section-title" style="top:80px">Built for Small &amp; Mid-Size Manufacturers</h2>
  <p class="section-sub" style="top:116px">You don't need to hire a full-time food safety director or figure out SQF alone. We bring<br>the expertise and technology you stay focused on production.</p>
  <svg class="abs" style="left:0;top:0" width="1200" height="744" viewBox="0 0 1200 744">
    <path d="M600 175L770 263V473L600 582L430 473V263Z" fill="none" stroke="var(--royal)" stroke-width="16" stroke-linejoin="round"/>
    <circle cx="600" cy="393" r="152" fill="#ffffff"/>
    <circle cx="600" cy="393" r="148" fill="none" stroke="var(--royal)" stroke-width="16"/>
    <circle cx="600" cy="393" r="134" fill="#ffffff" stroke="#d6d5f5" stroke-width="2"/>
    <defs><linearGradient id="whyPhoto" x1="0" y1="0" x2="1" y2="1"><stop offset="0" stop-color="#e4e6ec"/><stop offset="1" stop-color="#7d8ba3"/></linearGradient></defs>
    <circle cx="600" cy="393" r="126" fill="url(#whyPhoto)" role="img" aria-label="Photo of a food safety manager reviewing a checklist on a tablet"/>
    <g fill="#fff" stroke="#d3d2f6" stroke-width="3">
      <circle cx="424" cy="284" r="30"/><circle cx="779" cy="284" r="30"/>
      <circle cx="429" cy="478" r="30"/><circle cx="771" cy="478" r="30"/>
      <circle cx="600" cy="588" r="30"/>
    </g>
    <g fill="none" stroke="var(--royal)" stroke-width="1.6">
      <circle cx="424" cy="284" r="11"/><path d="M418 290l12-12"/>
      <rect x="767" y="274" width="24" height="18" rx="2"/><path d="M772 280h6M772 285h10"/>
      <path d="M419 489l10-20 10 20z"/><path d="M429 477v6"/>
      <circle cx="774" cy="472" r="7"/><path d="M760 490h12l8-5"/>
      <circle cx="600" cy="583" r="5"/><path d="M590 598c2-6 6-8 10-8s8 2 10 8"/>
    </g>
  </svg>
  <div class="feature left" style="left:120px;top:252px"><h4>Lower Cost Than a Full-Time Hire</h4><p>Get a complete SQF team program design, digital implementation, and coaching at a fraction of the cost of hiring a full-time SQF Practitioner.</p></div>
  <div class="feature" style="left:822px;top:252px"><h4>Your Program Lives in Software</h4><p>No more binders and spreadsheets. Your SQF system is built into PlantLedger or SafeSheet.io organized, accessible, and always audit-ready.</p></div>
  <div class="feature left" style="left:124px;top:448px"><h4>Flexible, Low-Risk Engagement</h4><p>Start with a 3-month commitment, then go month-to-month. Cancel anytime with 30 days notice. We earn your business</p></div>
  <div class="feature" style="left:815px;top:448px"><h4>Bilingual Floor-Level Support</h4><p>With our Central America team, we provide training and documentation in Spanish so every member of your production team understands and follows the program.</p></div>
  <div class="abs" style="left:0;width:1200px;top:636px;text-align:center">
    <h4 style="font-size:14.5px;font-weight:500;margin-bottom:4px">You Own It, We Support It</h4>
    <p style="font-size:10.5px;line-height:17.5px;color:var(--body)">We build the system and train your team. You maintain and run it day-to-day.<br>We stay on call with coaching and advisory so you never feel stuck.</p>
  </div>
</section>

<section class="process">
  <div class="eyebrow" style="top:58px">HOW IT WORKS</div>
  <h2 class="section-title" style="top:80px">From Discovery to Certification</h2>
  <p class="section-sub" style="top:118px">A clear, structured path that takes the guesswork out of SQF.</p>
  <div class="step-num" style="left:142px">01</div>
  <div class="step-num" style="left:406px">02</div>
  <div class="step-num" style="left:636px">03</div>
  <div class="step-num" style="left:866px">04</div>
  <svg class="abs" style="left:0;top:0" width="1200" height="440" viewBox="0 0 1200 440">
    <path d="M122 226H346L372 296L346 364H122Z" fill="#fff" stroke="#e4e3f7"/>
    <path d="M352 226H579L605 296L579 364H352L378 296Z" fill="#fff" stroke="#e4e3f7"/>
    <path d="M585 226H812L838 296L812 364H585L611 296Z" fill="#fff" stroke="#e4e3f7"/>
    <path d="M818 226H1050L1076 296L1050 364H818L844 296Z" fill="#fff" stroke="#e4e3f7"/>
    <g fill="none" stroke="var(--royal)" stroke-width="6" stroke-linejoin="miter">
      <path d="M342 226L368 296L342 364"/>
      <path d="M575 226L601 296L575 364"/>
      <path d="M808 226L834 296L808 364"/>
    </g>
  </svg>
  <div class="step" style="left:144px;width:185px"><h4>Discovery Call</h4><p>We learn about your facility, your current systems, and where you are in the SQF journey. No pressure just a conversation.</p></div>
  <div class="step" style="left:406px;width:160px"><h4>Gan Assessment</h4><p>We evaluate your facility against SQI requirements, identify what's missing, and give you a clear roadmap with priorities.</p></div>
  <div class="step" style="left:637px;width:165px"><h4>Build &amp; Implement</h4><p>We design your SQF program and build it directly into your digital food safety platform forms, logs, SOPs, HACCP plans, all of it.</p></div>
  <div class="step" style="left:868px;width:170px"><h4>Coach &amp; Certify</h4><p>We train your team, run mock audits, and prepare you for certification day. Then we stay on as your ongoing SQF advisory partner.</p></div>
</section>

<section class="testimonial">
  <div class="testimonial-panel">
    <div class="quote-mark">“</div>
    <p class="quote-text">"Northbay Compliance Group didn't just hand us a binder. They built our entire SQF system into software and coached our team until we owned it. We passed our first audit with confidence."</p>
    <div class="quote-cite">– SQF-Certified Manufacturing Client</div>
    <div class="testimonial-photo photo" role="img" aria-label="Photo of a worker in a lab coat and hairnet checking a clipboard beside a filling line"></div>
  </div>
</section>

<svg class="footer-bg" width="1200" height="395" viewBox="0 0 1200 395">
  <path d="M0 40Q200 40 200 140V395H0Z" fill="var(--navy-deep)"/>
  <path d="M1200 40Q1000 40 1000 140V395H1200Z" fill="var(--navy-deep)"/>
  <rect x="100" y="110" width="1000" height="285" fill="var(--navy-deep)"/>
  <path d="M0 110Q60 60 124 40" fill="none" stroke="var(--royal)" stroke-width="4"/>
  <path d="M1200 110Q1140 60 1076 40" fill="none" stroke="var(--royal)" stroke-width="4"/>
</svg>

<section class="cta">
  <h2>Start Manufacturing with Confidence</h2>
  <p>Partner with a trusted food &amp; beverage manufacturer committed to quality, safety, and scalability.</p>
  <a class="btn btn-white" style="left:381px;top:120px;width:190px;height:40px">REQUEST A QUOTE TODAY
    <svg viewBox="0 0 16 16" fill="none" stroke="var(--royal)" stroke-width="1.3"><path d="M8 1.5l5.5 2v4.2c0 3.3-2.4 5.6-5.5 6.8-3.1-1.2-5.5-3.5-5.5-6.8V3.5z"/><path d="M5.6 8l1.7 1.7 3.2-3.3"/></svg></a>
</section>

<footer class="footer">
  <div class="brand" style="left:130px;top:3540px">
    <span class="brand-dot" style="border-color:#fff"></span>
    <div><div class="brand-name" style="color:#fff">Northbay Compliance Group</div><div class="brand-tag" style="color:#fff">FOOD SAFETY &amp; SQF CERTIFICATION</div></div>
  </div>
  <p class="footer-about">Northbay Compliance Group LLC specializes in SQF food safety consulting, offering comprehensive guidance to food and beverage companies to achieve the highest standards in compliance, quality assurance, and risk management.</p>
  <div class="footer-col-rule" style="left:389px"></div>
  <div class="footer-col-rule" style="left:627px"></div>
  <div class="footer-col-rule" style="left:894px"></div>
  <h5 style="left:446px;top:3547px">Quick Links</h5>
  <div class="foot-link" style="top:3584px">Home</div>
  <div class="foot-link" style="top:3606px">Services</div>
  <div class="foot-link" style="top:3628px">Benefits</div>
  <div class="foot-link" style="top:3650px">Process</div>
  <div class="foot-link" style="top:3672px">Contact</div>
  <h5 style="left:669px;top:3550px">Contact Us</h5>
  <div class="foot-row" style="left:669px;top:3580px"><span class="foot-ic"><svg viewBox="0 0 10 10" fill="none" stroke="#fff" stroke-width="1"><path d="M2 1h2l1 2-1.2 1a5 5 0 0 0 2.2 2.2L7 5l2 1v2c-4 .5-8-3.5-7-7z"/></svg></span>+1 555-010-4420</div>
  <div class="foot-row" style="left:669px;top:3612px"><span class="foot-ic"><svg viewBox="0 0 10 10" fill="none" stroke="#fff" stroke-width="1"><rect x="1" y="2.5" width="8" height="5.5"/><path d="M1 2.5l4 3 4-3"/></svg></span>hello@northbaycompliance.com</div>
  <h5 style="left:955px;top:3550px">Follow Us</h5>
  <div class="foot-row" style="left:955px;top:3578px"><span class="foot-ic"></span>Facepage</div>
  <div class="foot-row" style="left:955px;top:3613px"><span class="foot-ic"></span>WorkLink</div>
  <div class="foot-row" style="left:955px;top:3647px"><span class="foot-ic"></span>Snapgram</div>
  <div class="copyright">Copyright © Northbay Compliance Group 2026 All Rights Reserved</div>
</footer>

</body>
</html>
```